Quilvo Garage Doors Business Card

I need a Business Card for my garage door business:
Quilvo Garage Doors.
please add:
logo
phone number: 855-3-QUILVO
(853-392)

email: service@quilvogaragedoors.com
website: www.quilvogaragedoors.com

The attached image is recommendation ONLY.

```html
<!DOCTYPE html>
<html lang="en">
<head>
<meta charset="utf-8">
<title>Quilvo Garage Doors – Business Card</title>
<link rel="stylesheet" href="https://fonts.googleapis.com/css2?family=Asap:wght@400;500&display=swap">
<style>
  :root {
    --backdrop: #3b3b3b;
    --paper: #ffffff;
    --teal: #5bc3d0;
    --teal-deep: #3f9c9a;
    --ink: #1c1c1c;
    --ink-soft: #333333;
    --white: #ffffff;
  }
  * { margin: 0; padding: 0; box-sizing: border-box; }
  html, body {
    width: 1200px; height: 820px; overflow: hidden;
    background: var(--backdrop);
    font-family: "Asap", Arial, sans-serif;
  }
  .canvas { position: relative; width: 1200px; height: 820px; }
  .card {
    position: absolute; top: 258px;
    width: 477px; height: 272px; overflow: hidden;
  }
  .card--front { left: 115px; background: var(--paper); }
  .card--back { left: 621px; }

  .brand { position: absolute; left: 78px; top: 45px; display: flex; align-items: center; }
  .brand__dot {
    width: 58px; height: 58px; border-radius: 50%;
    background: var(--teal); margin-right: 54px;
  }
  .brand__name {
    font-weight: 500; font-size: 33px; line-height: 36px;
    color: var(--ink);
  }

  .call { position: absolute; left: 0; right: 0; top: 149px; text-align: center; }
  .call__label { font-size: 18px; color: var(--teal); }
  .call__phone {
    margin-top: 4px; font-size: 23px; color: var(--ink-soft);
    display: flex; justify-content: center; align-items: center; gap: 10px;
  }
  .call__phone svg { width: 18px; height: 18px; fill: var(--teal); }

  .contact-band {
    position: absolute; left: 0; right: 0; top: 224px; height: 28px;
    background: var(--teal); color: var(--white); font-size: 14px;
    display: flex; justify-content: center; align-items: center; gap: 8px;
  }
  .contact-band svg { width: 12px; height: 12px; fill: var(--white); }
  .contact-band__divider { width: 1px; height: 16px; background: var(--white); margin: 0 4px; }

  .team-photo {
    position: absolute; inset: 0;
    background: linear-gradient(180deg, #3f9a8d 0%, #58b0a8 45%, #62b8b6 100%);
  }
  .back-name {
    position: absolute; left: 0; right: 0; top: 126px; text-align: center;
    font-weight: 500; font-size: 24px; color: var(--white);
  }
  .web-band {
    position: absolute; left: 0; right: 0; top: 234px; height: 28px;
    background: rgba(110, 200, 205, 0.75);
    display: flex; justify-content: center; align-items: center;
    font-size: 15px; color: var(--ink);
  }
</style>
</head>
<body>
<main class="canvas">
  <section class="card card--front">
    <div class="brand">
      <span class="brand__dot"></span>
      <span class="brand__name">Quilvo<br>Garage Doors</span>
    </div>
    <div class="call">
      <p class="call__label">Call Us</p>
      <p class="call__phone">
        <svg viewBox="0 0 24 24" aria-hidden="true"><path d="M6.6 10.8a15.1 15.1 0 0 0 6.6 6.6l2.2-2.2a1 1 0 0 1 1-.25 11.4 11.4 0 0 0 3.6.57 1 1 0 0 1 1 1V20a1 1 0 0 1-1 1A17 17 0 0 1 3 4a1 1 0 0 1 1-1h3.5a1 1 0 0 1 1 1c0 1.25.2 2.45.57 3.6a1 1 0 0 1-.25 1z"/></svg>
        (853) 392-0147
      </p>
    </div>
    <div class="contact-band">
      <svg viewBox="0 0 24 24" aria-hidden="true"><path d="M2 5h20v14H2z M2 5l10 8 10-8" /></svg>
      <span>service@quilvogaragedoors.com</span>
      <span class="contact-band__divider"></span>
      <svg viewBox="0 0 24 24" aria-hidden="true"><circle cx="12" cy="12" r="10"/></svg>
      <span>www.quilvogaragedoors.com</span>
    </div>
  </section>

  <section class="card card--back">
    <div class="team-photo" role="img" aria-label="Team photo: service crew standing beside a branded service truck in front of trees, tinted teal"></div>
    <p class="back-name">Quilvo Garage Doors</p>
    <div class="web-band">www.quilvogaragedoors.com</div>
  </section>
</main>
</body>
</html>
```